VentureListingsHubNow.com - website
Business Opportunity website
VentureListingsHubNow.com - website - Advertising
Creative Brief
Advertising
We are an advertising site that lists available business opportunities. Advertisers pay us to post their opportunities and visitors can view, contact business opportunities.
http://www.tradeploverlink.example/
http://www.marketventurely.example/
-Listings to be displayed in 4 columns like uploaded image example. -Cart Form for requesting info... up to 10 opportunities at a time. -3 search fields: 1/ industry 2/ price 3/ location - navigation 1/Home 2/ Advertise 3/ Contact - navigation bottom 1/Home 2/ Advertise 3/ Contact 4/ Privacy - Prospect Lantern Bulletin

```html
<!DOCTYPE html>
<html lang="en">
<head>
<meta charset="utf-8">
<title>VentureListingsHubNow.com</title>
<link href="https://fonts.googleapis.com/css2?family=Open+Sans:wght@400;600;700&display=swap" rel="stylesheet">
<style>
:root{
  --blue-dark:#0e4a85;
  --blue:#1b6db4;
  --blue-light:#3a95db;
  --orange:#f39a1c;
  --orange-dark:#e07f0a;
  --card-top:#eaf4fc;
  --card-bottom:#b6d5ee;
  --grey-bg:#eff1f3;
  --grey-panel:#dfe3e7;
  --text:#3b3b3b;
  --white:#ffffff;
}
*{box-sizing:border-box;margin:0;padding:0}
html,body{width:1200px;height:1027px;overflow:hidden}
body{position:relative;background:var(--grey-bg);font-family:"Open Sans",Verdana,sans-serif;color:var(--text)}
.abs{position:absolute}

.top-rule{left:0;top:0;width:1200px;height:8px;background:var(--blue)}
.header{left:0;top:8px;width:1200px;height:137px;background:var(--white)}
.brand{left:125px;top:34px;display:flex;align-items:center;gap:12px}
.brand-dot{width:30px;height:30px;border-radius:50%;background:var(--orange)}
.brand-name{font-size:27px;font-weight:700;color:var(--blue-dark);letter-spacing:-.5px}
.account-links{left:858px;top:76px;font-size:13px;color:var(--blue)}
.account-links span{margin:0 10px;color:var(--orange)}

.hero-band{left:0;top:145px;width:1200px;height:233px;background:linear-gradient(var(--blue-dark),var(--blue) 40%,var(--blue-light))}
.main-nav{left:120px;top:113px;display:flex;gap:4px}
.main-nav a{display:block;height:32px;padding:6px 24px 0;background:var(--blue-dark);color:var(--white);font-size:14px;font-weight:600;text-decoration:none;border-radius:10px 10px 0 0}
.search-label{left:734px;top:112px;font-size:14px;font-weight:600;color:var(--orange)}
.search-box{left:827px;top:103px;width:253px;height:34px;background:var(--white);border-radius:17px;border:2px solid #c9d4de;display:flex;align-items:center;padding-left:12px}

.intro{left:120px;top:167px;width:690px;height:203px;background:var(--white);padding:14px 20px;box-shadow:0 2px 4px rgba(0,0,0,.25)}
.intro h1{font-size:21px;font-weight:700;color:var(--blue);margin-bottom:6px}
.intro p{font-size:11.6px;line-height:15.5px;margin-bottom:10px}

.featured{left:830px;top:159px;width:250px;height:211px;background:var(--grey-panel);padding:7px 8px}
.featured h2{background:#b9c1c9;color:var(--white);font-size:12px;font-weight:700;text-align:center;padding:3px 0;letter-spacing:1px;margin-bottom:5px}
.featured-item{font-size:10px;line-height:13px;color:#666;border-bottom:1px solid #c3c9cf;padding:3px 6px 2px;margin-bottom:3px}
.featured-item .more{display:block;text-align:right;color:var(--orange-dark)}

.listings{left:120px;top:404px;width:690px;height:509px;background:var(--blue-dark);border:4px solid var(--orange);border-radius:6px}
.filter-bar{height:40px;background:var(--orange);display:flex;align-items:center;padding:0 8px;gap:10px;font-size:15px;color:var(--blue-dark);font-weight:600}
.filter-bar .field{width:110px;height:20px;background:var(--white);margin-right:28px}
.filter-bar .search-btn{margin-left:auto;background:var(--white);color:var(--orange-dark);font-size:13px;font-weight:700;padding:3px 14px;border-radius:12px}
.grid{display:grid;grid-template-columns:repeat(4,159px);grid-auto-rows:212px;gap:16px 13px;padding:6px 7px}
.card{background:linear-gradient(var(--card-top),var(--card-bottom));border-radius:6px;position:relative}
.request-btn{position:absolute;top:-2px;left:50%;transform:translateX(-50%);background:var(--orange);color:var(--white);font-size:10.5px;font-weight:700;padding:2px 14px;border-radius:9px;white-space:nowrap}

.cart{left:830px;top:404px;width:250px;height:509px;background:var(--white);border:4px solid var(--blue);border-radius:6px;overflow:hidden}
.cart h2{background:var(--orange);color:var(--white);font-size:12px;font-weight:700;text-align:center;padding:8px 0;letter-spacing:1px}
.cart-rows{height:100%;margin:6px 10px;background:repeating-linear-gradient(var(--white) 0 47px,#9fb7cc 47px 48px)}

.footer-nav{left:134px;top:934px;display:flex;gap:26px;font-size:13px;color:var(--blue-dark);font-weight:600}
.footer-band{left:0;top:960px;width:1200px;height:67px;background:linear-gradient(var(--blue),var(--blue-dark));color:var(--white);font-size:11px;font-weight:600;text-align:center;padding-top:26px}
</style>
</head>
<body>
<div class="abs top-rule"></div>
<header class="abs header"></header>
<div class="abs brand"><div class="brand-dot"></div><div class="brand-name">VentureListingsHubNow.com</div></div>
<div class="abs account-links">Log In<span>|</span>Register<span>|</span>Contact Us</div>

<div class="abs hero-band"></div>
<nav class="abs main-nav"><a href="#">Home</a><a href="#">Advertise</a><a href="#">Contact</a></nav>
<div class="abs search-label">Search Here:</div>
<div class="abs search-box">
  <svg width="22" height="22" viewBox="0 0 22 22"><circle cx="9" cy="9" r="6" fill="none" stroke="#9aa8b5" stroke-width="2.5"/><line x1="13.5" y1="13.5" x2="20" y2="20" stroke="#9aa8b5" stroke-width="3" stroke-linecap="round"/></svg>
</div>

<section class="abs intro">
  <h1>Lorem Ipsum</h1>
  <p>Lorem Ipsum is simply dummy text of the printing and typesetting industry. Lorem Ipsum has been the industry's standard dummy text ever since the 1500s, when an unknown printer took a galley of type and scrambled it to make a type specimen book. It has survived not only five centuries, but also the leap into electronic typesetting, remaining essentially unchanged. It was popularised in the 1960s with the release of Marqueline sheets containing Lorem Ipsum passages, and more recently with desktop publishing software like Folioset Press including versions of Lorem Ipsum.</p>
  <p>Lorem Ipsum is simply dummy text of the printing and typesetting industry. Lorem Ipsum has been the industry's standard dummy text ever since the 1500s, when an unknown printer took a galley of type and scrambled it to make a type specimen book. It has survived not only five centuries, but also the leap into electronic typesetting.</p>
</section>

<aside class="abs featured">
  <h2>FEATURED BIZ</h2>
  <div class="featured-item">Lorem Ipsum is simply dummy text of the printing and typesetting industry. Lorem Ipsum has been the...<span class="more">See more...</span></div>
  <div class="featured-item">Lorem Ipsum is simply dummy text of the printing and typesetting industry. Lorem Ipsum has been the...<span class="more">See more...</span></div>
  <div class="featured-item">Lorem Ipsum is simply dummy text...<span class="more">See more...</span></div>
</aside>

<section class="abs listings">
  <div class="filter-bar">
    Industry <div class="field"></div>
    Price <div class="field"></div>
    Location <div class="field"></div>
    <div class="search-btn">SEARCH</div>
  </div>
  <div class="grid">
    <div class="card"><span class="request-btn">Request Info</span></div>
    <div class="card"><span class="request-btn">Request Info</span></div>
    <div class="card"><span class="request-btn">Request Info</span></div>
    <div class="card"><span class="request-btn">Request Info</span></div>
    <div class="card"><span class="request-btn">Request Info</span></div>
    <div class="card"><span class="request-btn">Request Info</span></div>
    <div class="card"><span class="request-btn">Request Info</span></div>
    <div class="card"><span class="request-btn">Request Info</span></div>
  </div>
</section>

<aside class="abs cart">
  <h2>CART - REQUEST INFO</h2>
  <div class="cart-rows"></div>
</aside>

<nav class="abs footer-nav"><span>Home</span><span>Advertise</span><span>Contact</span><span>Privacy</span></nav>
<footer class="abs footer-band">Copyright © VentureListingsHubNow.com. All rights reserved.</footer>
</body>
</html>
```